Korbin Ventilation's. "Clean air, done right"!

Good day< Does your company do face mask? that is question 1. and lets finish the stationary design and I will pay for that now? 2 If your company has BLACK HATS now I would want to do some of those? 3 I notice do you do BANNER'S and or something I can put on van's magnet type or on a building! )k that's enough but for now lets start with the stationary stuff? let me know you should have my information, and the design look's GREAT!!! Thank you..

```html
<!DOCTYPE html>
<html lang="en">
<head>
<meta charset="utf-8">
<title>Korbin Ventilation's Letterhead</title>
<link rel="stylesheet" href="https://fonts.googleapis.com/css2?family=Poppins:wght@400;500&family=Didact+Gothic&display=swap">
<style>
  :root {
    --paper: #e2e2e2;
    --ink: #1c1c1c;
    --ink-soft: #3a3a3a;
    --rule: #2a2a2a;
    --band-dark: #0a0a0a;
    --band-sage: #a9ad88;
  }
  * { margin: 0; padding: 0; box-sizing: border-box; }
  html, body { width: 960px; height: 1200px; overflow: hidden; background: var(--paper); }
  .letterhead {
    position: relative;
    width: 960px;
    height: 1200px;
    background: var(--paper);
    color: var(--ink);
    font-family: "Didact Gothic", "Century Gothic", sans-serif;
  }
  .brand {
    position: absolute;
    left: 84px;
    top: 96px;
    width: 210px;
    text-align: center;
  }
  .brand-dot {
    display: block;
    width: 62px;
    height: 62px;
    margin: 0 auto 10px;
    border-radius: 50%;
    background: var(--ink);
  }
  .brand-name {
    font-family: "Poppins", sans-serif;
    font-weight: 500;
    font-size: 22px;
    line-height: 1.15;
    color: var(--ink);
  }
  .brand-tagline {
    margin-top: 6px;
    font-family: "Poppins", sans-serif;
    font-weight: 500;
    font-size: 13px;
    color: var(--ink);
  }
  .contact {
    position: absolute;
    left: 620px;
    top: 95px;
    height: 134px;
    padding-left: 26px;
    border-left: 1.5px solid var(--rule);
    font-family: "Poppins", sans-serif;
    font-style: normal;
    font-size: 14px;
    line-height: 16.5px;
    color: var(--ink-soft);
  }
  .contact-company { color: var(--ink); font-weight: 500; }
  .contact-address { margin-bottom: 5px; }
  .contact-list { list-style: none; }
  .contact-list li { display: flex; align-items: center; gap: 9px; }
  .contact-list svg { width: 12px; height: 12px; fill: var(--ink); flex: none; }
  .greeting {
    position: absolute;
    left: 88px;
    top: 352px;
    font-size: 22px;
    color: var(--ink);
  }
  .body-copy {
    position: absolute;
    left: 88px;
    top: 414px;
    width: 792px;
    font-size: 13.6px;
    line-height: 18.3px;
    letter-spacing: 0.3px;
    color: var(--ink-soft);
    text-align: justify;
    hyphens: auto;
  }
  .body-copy p + p { margin-top: 18.3px; }
  .closing {
    position: absolute;
    left: 88px;
    top: 802px;
    font-size: 13.6px;
    color: var(--ink-soft);
  }
  .signature {
    position: absolute;
    left: 88px;
    top: 846px;
    width: 124px;
    height: 64px;
    background: linear-gradient(180deg, #d6d6d6, #cacaca);
  }
  .footer-band {
    position: absolute;
    left: 0;
    bottom: 0;
    width: 960px;
    height: 10px;
  }
</style>
</head>
<body>
  <main class="letterhead">
    <header>
      <div class="brand">
        <span class="brand-dot"></span>
        <div class="brand-name">Korbin Ventilation's</div>
        <div class="brand-tagline">"Clean air, done right"</div>
      </div>

      <address class="contact">
        <div class="contact-company">Korbin Ventilation's LLC</div>
        <div>4120 Birchwood Court</div>
        <div class="contact-address">Fairbanks, Alaska 99701</div>
        <ul class="contact-list">
          <li><svg viewBox="0 0 12 12"><path d="M2.4 0.6l2 2.1-1 1.4c.7 1.6 2 2.9 3.6 3.6l1.4-1 2.1 2-1.2 2.2C4.9 10.6 1.4 7.1.3 2.6z"/></svg>555-214-0381</li>
          <li><svg viewBox="0 0 12 12"><path d="M3 0h6v12H3zM4.2 1.3v8h3.6v-8zM5.4 10.1h1.2v1H5.4z" fill-rule="evenodd"/></svg>555-630-2974</li>
          <li><svg viewBox="0 0 12 12"><path d="M3 1h6v3H3zM1 5h10v5H9V8H3v2H1zM3.5 8.8h5V12h-5z"/></svg>555-418-7726</li>
          <li><svg viewBox="0 0 12 12"><path d="M1 3h10v6.5H1zM1.5 3.4L6 6.6l4.5-3.2"/></svg>info@korbinventilations.com</li>
          <li><svg viewBox="0 0 12 12"><path d="M6 .5a5.5 5.5 0 1 0 0 11 5.5 5.5 0 0 0 0-11zM4 3.2c1 .2 1.6.9 1.3 1.8-.3.8-1.5.6-1.5 1.7 0 .9.9 1.3.6 2.4C2.8 8.5 1.8 7 2 5.2c.4-.9 1-1.6 2-2zM8 4.3c.8.5 1.2 1.7.8 2.8-.5-.6-1.2-.5-1.6-1.2-.3-.7.2-1.3.8-1.6z"/></svg>www.korbinventilations.com</li>
        </ul>
      </address>
    </header>

    <p class="greeting">Dear Mr. Carter,</p>

    <section class="body-copy">
      <p>Lorem ipsum dolor sit amet, consectetur adipiscing elit. Donec orci purus, luctus vitae dignissim eu, iaculis sed purus. Vivamus faucibus, ipsum nec aliquet viverra, leo mauris condimentum ligula, sit amet sagittis enim ligula quis arcu. Nam egestas tortor id nisi porttitor mattis. In tortor ante, ultricies in suscipit a, tempus non massa. Vivamus et auctor mi. Fusce vel massa nulla. Phasellus nec eros mauris, et scelerisque orci.</p>
      <p>Donec malesuada orci vitae nulla accumsan porta a id massa. Quisque accumsan iaculis magna sit amet fringilla. Maecenas consequat, magna eget tincidunt semper, odio nibh rutrum mi, id feugiat ante nisi eu risus. Vestibulum nunc orci, rhoncus a placerat in, ultricies in mi. Cras mattis varius eros, vel fringilla nisi suscipit eget. Quisque scelerisque sagittis nulla at porttitor.</p>
      <p>Sed id augue vitae urna euismod commodo aliquet a quam. Pellentesque arcu velit, cursus et malesuada ut, consequat et diam. Nullam erat sem, rhoncus id ullamcorper vitae, rhoncus et arcu. In ultricies ultricies nulla, ut rutrum nisi iaculis at. Donec eu magna a metus ornare faucibus. Fusce aliquet faucibus ultricies. Morbi semper, est id tincidunt gravida, sem arcu adipiscing lacus, ac bibendum nulla leo eu purus. Quisque nec diam sed risus consectetur a ccumsan quis quis nibh. Vestibulum id purus lorem.</p>
      <p>It is a long established fact that a reader will be distracted by the readable content of a page when looking at its layout. The point of using Lorem Ipsum is that it has a more-or-less normal distribution of letters, as opposed to using 'Content here, content here', making it look like readable English. Many desktop publishing packages</p>
    </section>

    <p class="closing">Sincerely,</p>
    <div class="signature" role="img" aria-label="Handwritten signature of the sender"></div>

    <svg class="footer-band" viewBox="0 0 960 10" preserveAspectRatio="none" aria-hidden="true">
      <polygon points="790,0 960,0 960,10 800,10" fill="var(--band-sage)"/>
      <polygon points="0,0 788,0 798,10 0,10" fill="var(--band-dark)"/>
    </svg>
  </main>
</body>
</html>
```